Letterhead for 3 attorney Workers' Comp law firm

We are a 3 attorney law office. We specialize in Workers' Compensation. Our office represents workers who are injured on the job, and the estates of workers who are killed one the job.
When we started our office, we created our own letterhead & have been using it for years. We've just recently hired the 3rd attorney, and were going to just add his name to the letterhead, but have decided we wanted to get a professionally designed letterhead and business cards at this point.
We want something that looks clean and professional. It must look good in black and white because we often make multiple copies of our documents. We're hoping for a design that resonates confidence, reliability and experience.
The design must include the firm name: Dorrance & Pike, PLLC. We would like the PLLC to be small compared to the Dorrance & Pike graphic. We also want to incorporate the attorney names: Ulric Dorrance, Janet Pike, and Lyle Hagberg. Our current letterhead has our contact info in the footer at the bottom of the page. We like that design, but are open to the idea of having it at the top. We'll leave that at the discretion of the designer. Our contact info is as follows: 472 S. Larchmont Avenue, Suite 315 Bellingham, WA 98117 Phone: 360-514-2967, Fax: 360-521-6079, and our website: www.dorrancepike-law.example
Target Market(s)
Clients, courts, other legal offices, doctors offices. These are the people who see our letterhead most frequently. It's not so much for marketing purposes, mainly so that we have a professional image when sending out documents.
Industry/Entity Type
Law Firm
Contact Information for Business Card
On the back of the business card: it can be designed, or be a template for filling in appointment reminder information (i.e. date, time, etc)
Colors
Designer to choose colors to be used in the design.
Requirements
Must have
- Must have our firm name at the top.
- Must include the attorney names.
- Must have all of our contact information (can be at top or bottom - whatever looks best with the design)
Nice to have
- A strong, confident design
Should not have
- We don't want the design to be playful, cartoony or busy.

```html
<!DOCTYPE html>
<html lang="en">
<head>
<meta charset="utf-8">
<title>Dorrance &amp; Pike, PLLC — Letterhead Options</title>
<link href="https://fonts.googleapis.com/css2?family=Source+Sans+3:wght@400;600;700&family=Crimson+Pro:wght@400;600&display=swap" rel="stylesheet">
<style>
  :root {
    --backdrop: #dcdddf;
    --paper: #ffffff;
    --ink: #1d1d1f;
    --blue-bright: #1672bd;
    --blue-deep: #0f5b82;
    --sans: "Source Sans 3", Arial, sans-serif;
    --serif: "Crimson Pro", Georgia, serif;
  }
  * { margin: 0; padding: 0; box-sizing: border-box; }
  html, body { width: 1200px; height: 796px; overflow: hidden; }
  body { background: var(--backdrop); position: relative; color: var(--ink); }

  .sheet {
    position: absolute; top: 51px; width: 536px; height: 694px;
    background: var(--paper);
    box-shadow: 0 1px 4px rgba(0,0,0,0.18);
  }
  .sheet--sans { left: 51px; font-family: var(--sans); }
  .sheet--serif { left: 613px; font-family: var(--serif); }

  .firm-name {
    position: absolute; left: 26px; top: 22px;
    line-height: 1; white-space: nowrap;
  }
  .firm-name__main { display: block; }
  .firm-name__suffix { font-size: 0.55em; }
  .sheet--sans .firm-name { color: var(--blue-bright); font-weight: 600; font-size: 25px; letter-spacing: 0.5px; }
  .sheet--serif .firm-name { color: var(--blue-deep); font-weight: 600; font-size: 27px; letter-spacing: 0.5px; }
  .firm-name__line2 { display: block; padding-left: 22px; margin-top: 2px; }

  .address, .contact, .attorneys {
    position: absolute; right: 25px; text-align: right; white-space: nowrap;
  }
  .address { top: 22px; font-size: 7.6px; }
  .contact { top: 33px; font-size: 7.6px; display: flex; gap: 14px; align-items: center; }
  .contact__item { display: inline-flex; align-items: center; gap: 3px; }
  .contact__label { font-weight: 600; color: var(--blue-deep); }
  .icon { width: 7px; height: 7px; fill: var(--blue-bright); }

  .rule-top { position: absolute; right: 25px; height: 2px; }
  .sheet--sans .rule-top { top: 45px; left: 141px; background: var(--blue-bright); }
  .sheet--serif .rule-top { top: 46px; left: 88px; background: var(--blue-deep); }

  .attorneys { top: 55px; display: flex; gap: 8px; }
  .sheet--sans .attorneys { font-size: 9.8px; font-weight: 700; }
  .sheet--serif .attorneys { font-size: 10.4px; font-weight: 600; top: 56px; }
  .attorneys__sep { font-weight: 400; }

  .footer { position: absolute; left: 26px; right: 25px; }
  .footer--double { top: 661px; height: 14px; }
  .footer__thin { position: absolute; left: 0; right: 0; top: 3px; height: 2px; background: var(--blue-bright); }
  .footer__thick { position: absolute; left: 0; right: 0; top: 10px; height: 3.5px; background: var(--blue-bright); }
  .footer__web {
    position: absolute; left: 50%; top: -3px; transform: translateX(-50%);
    background: var(--paper); padding: 0 7px;
    font-size: 9.6px; font-weight: 700; white-space: nowrap;
  }
  .footer--single { top: 672px; height: 2px; background: var(--blue-deep); }
</style>
</head>
<body>

<section class="sheet sheet--sans" aria-label="Letterhead option one">
  <h1 class="firm-name">
    <span class="firm-name__main">Dorrance &amp;</span>
    <span class="firm-name__line2">Pike<span class="firm-name__suffix">, PLLC</span></span>
  </h1>
  <p class="address">472 S. Larchmont Avenue, Suite 315 Bellingham, WA 98117</p>
  <p class="contact">
    <span class="contact__item">
      <svg class="icon" viewBox="0 0 10 10" aria-hidden="true"><path d="M2 0.5 L3.6 0.5 L4.3 2.8 L3.1 3.7 Q4.2 6 6.3 6.9 L7.2 5.7 L9.5 6.4 L9.5 8 Q9.5 9.5 8 9.5 Q1 9 0.5 2 Q0.5 0.5 2 0.5 Z"/></svg>
      360-514-2967
    </span>
    <span class="contact__item">
      <svg class="icon" viewBox="0 0 10 10" aria-hidden="true"><rect x="2.5" y="0.5" width="5" height="3"/><rect x="0.5" y="3.5" width="9" height="4.5" rx="1"/><rect x="2.5" y="6.5" width="5" height="3"/></svg>
      360-521-6079
    </span>
  </p>
  <div class="rule-top"></div>
  <p class="attorneys">
    <span>Ulric Dorrance</span><span class="attorneys__sep">/</span>
    <span>Janet Pike</span><span class="attorneys__sep">/</span>
    <span>Lyle Hagberg</span>
  </p>
  <footer class="footer footer--double">
    <div class="footer__thin"></div>
    <div class="footer__thick"></div>
    <span class="footer__web">www.dorrancepike-law.example</span>
  </footer>
</section>

<section class="sheet sheet--serif" aria-label="Letterhead option two">
  <h1 class="firm-name">
    <span class="firm-name__main">Dorrance &amp;</span>
    <span class="firm-name__line2">Pike<span class="firm-name__suffix">, PLLC</span></span>
  </h1>
  <p class="address">472 S. Larchmont Avenue, Suite 315 Bellingham, WA 98117</p>
  <p class="contact">
    <span class="contact__item"><span class="contact__label">P:</span> 360-514-2967</span>
    <span class="contact__item"><span class="contact__label">F:</span> 360-521-6079</span>
    <span class="contact__item">www.dorrancepike-law.example</span>
  </p>
  <div class="rule-top"></div>
  <p class="attorneys">
    <span>Ulric Dorrance</span><span class="attorneys__sep">|</span>
    <span>Janet Pike</span><span class="attorneys__sep">|</span>
    <span>Lyle Hagberg</span>
  </p>
  <div class="footer footer--single"></div>
</section>

</body>
</html>
```